The Garden Under the Lantern: A Quiet Pilgrimage

This is a memoir about my breakdown/breakthrough followed by a spiritual awakening in 2012, I found my guru Hemant Sulori Dev, Mother Ayahuasca, and my spiritual mother, Lalu. By 2013, I was headed for a spiritual adventure through India, Southeast India, and Nepal which lasted 14 months. I lived in ashrams, meditated and prayed in temples,, traveled by train and bus, met many enlightened beings and interesting people. During Vipassana, I discovered my true essence- the light of my soul. It is a book of travel, romance, and spiritual growth. My idea is a road lined with temples, etc. I am walking down the road and see myself at the end of the road, facing out, with a bright star in my heart center. I see the colors in muted yellows and other earth-tone hues. Marigolds are used everywhere in the temples to adorn statues and doorways and this speaks to me. The title of the book is about finding out who I am beyond my stories and it is also about how our story will reveal to us who we really are.

Target Market(s)

Spiritual seekers, adventurers, travelers

Industry/Entity Type

Spiritual

Font styles to use
Serif
Sans Serif
Other font styles liked:
• I’m open. I like simplicity

Colors
FFC000
F8CF3A
FAE287
FDF2CF
FEFAEE

Requirements
Must have
• My name: Greta Lunara Ses, Earth tones, pastels, me or a likeness of me, room for ISBN on back cover
Nice to have
• In the photo uploads I drew an idea of what I would like, there is also the idea in the book
Should not have
• I am not a fan of bright colors and that's all I can select here. I like neutral colors, like browns, slate, creams, and whites. This reflects the dusty roads I took throughout my journey.

```html
<!DOCTYPE html>
<html lang="en">
<head>
<meta charset="utf-8">
<title>The Garden Under the Lantern — Book Cover</title>
<link rel="stylesheet" href="https://fonts.googleapis.com/css2?family=Kodchasan:wght@400&family=Pathway+Gothic+One&display=swap">
<style>
  :root {
    --backdrop: #000000;
    --paper: #f2f1ea;
    --oval: #c2b8ab;
    --ink-soft: #bcae9f;
    --road-line: #d3cbbf;
    --vignette: #dcd3c4;
    --title-ink: #f2f1ea;
  }
  html, body {
    margin: 0;
    padding: 0;
    width: 1200px;
    height: 1200px;
    overflow: hidden;
    background: var(--backdrop);
  }
  .canvas {
    width: 1200px;
    height: 1200px;
    display: block;
  }
  .cover-paper { fill: var(--paper); }
  .title-oval { fill: var(--oval); }
  .road-edge { fill: none; stroke: var(--road-line); stroke-width: 2; }
  .road-center { fill: none; stroke: var(--road-line); stroke-width: 2; stroke-dasharray: 26 20; }
  .vignette { fill: var(--vignette); }
  .traveler { fill: var(--vignette); opacity: 0.75; }
  .subtitle {
    font-family: "Kodchasan", sans-serif;
    font-size: 44px;
    fill: var(--ink-soft);
  }
  .title-line {
    font-family: "Pathway Gothic One", sans-serif;
    font-size: 132px;
    fill: var(--title-ink);
    letter-spacing: 1px;
  }
  .author {
    font-family: "Kodchasan", sans-serif;
    font-size: 34px;
    letter-spacing: 3px;
    fill: var(--ink-soft);
  }
</style>
</head>
<body>
<svg class="canvas" viewBox="0 0 1200 1200" xmlns="http://www.w3.org/2000/svg">
  <rect class="cover-paper" x="240" y="60" width="720" height="1080"/>

  <text class="subtitle" x="600" y="136" text-anchor="middle">A Quiet Pilgrimage</text>

  <g class="road">
    <path class="road-edge" d="M540 984 C 400 900, 324 760, 324 582 C 324 352, 448 168, 602 168 C 756 168, 880 352, 880 582 C 880 812, 756 996, 602 996 L 540 996 L 380 1016"/>
    <path class="road-center" d="M602 970 C 742 970, 854 796, 854 582 C 854 368, 742 196, 602 196 C 462 196, 350 368, 350 582 C 350 760, 420 900, 470 960 L 400 1000"/>
    <line class="road-edge" x1="380" y1="1020" x2="540" y2="1020"/>
  </g>

  <ellipse class="title-oval" cx="600" cy="600" rx="232" ry="372"/>

  <g class="journey-stops">
    <circle class="vignette" cx="384" cy="380" r="58" role="img" aria-label="Sepia illustration of a woman standing beneath a temple archway"/>
    <circle class="vignette" cx="344" cy="564" r="58" role="img" aria-label="Sepia illustration of a carved stone shrine"/>
    <circle class="vignette" cx="360" cy="768" r="58" role="img" aria-label="Sepia illustration of an arched palace facade"/>
    <circle class="vignette" cx="816" cy="380" r="58" role="img" aria-label="Sepia illustration of an ornate temple tower"/>
    <circle class="vignette" cx="860" cy="564" r="58" role="img" aria-label="Sepia illustration of a domed riverside temple"/>
    <circle class="vignette" cx="840" cy="768" r="58" role="img" aria-label="Sepia illustration of a stupa among trees"/>
  </g>

  <rect class="traveler" x="280" y="840" width="68" height="190" rx="30" role="img" aria-label="Line drawing of a woman traveler walking along the road"/>

  <g class="title" text-anchor="middle">
    <text class="title-line" x="600" y="368">THE</text>
    <text class="title-line" x="600" y="496" textLength="300" lengthAdjust="spacingAndGlyphs">GARDEN</text>
    <text class="title-line" x="600" y="624" textLength="266" lengthAdjust="spacingAndGlyphs">UNDER</text>
    <text class="title-line" x="600" y="752">THE</text>
    <text class="title-line" x="600" y="872" textLength="296" lengthAdjust="spacingAndGlyphs">LANTERN</text>
  </g>

  <text class="author" x="600" y="1096" text-anchor="middle">GRETA LUNARA SES</text>
</svg>
</body>
</html>
```